Packaging for Hair Extensions range

We are a successful hair extensions company who are looking at redesigning our current hair extensions packaging for a fresh and modern new look. We need a designer who is highly skilled and very modern and fashionable in their approach to design.

For this particular job need 1 piece of packaging designed but once the design is approved, we will need the design to be edited as we need it for two different product brand names. So, it will contain the same product (hair extensions) but each of the 2 packages will have different text, colours, and images.

The product is Pre Bonded hair. Please visit: http://www.velvetmuse.com.au/pre-bonded.php so you can see the product.

I have attached a document called "packaging example". this is the type of packaging we need. It will house 50cm long hair extensions. It consists of a long piece of card with a flap at the top. Unless you can think of a better way to display the hair. this link shows the hair it will contain:

http://www.larkspurhairextensions.com.au/pd_fusion_hair_extensions_diy_kits.cfm

The two different brand names are: Velvet Muse (www.velvetmuse.com.au) and larkspur hair extensions (www.larkspurhairextensions.com.au).

We also need a logo and website redesign for larkspur so would like to discuss that with the approved designer.

Please note:

We have many design jobs available each month as we own 3 different businesses and always need new posters, brochures, flyers, web banners and various other items designed, so the successful designer will recieve a constant stream of new work from us.

We need someone reliable who can stick to time frames as we are a fast moving company.

I look forward to seeing your design!

Target Market(s)

Women, aged between 18 and 45. Women who care about their appearance and want to look beautiful, modern, stylish and fashionable. Women who read fashion magazines and want to look like models. Women who want to be successful.

Industry/Entity Type

Larkspur

Requirements
Must have
• Designer must have an awareness of popular design looks and trends in the fashion, hair and beauty world.
Must be a high quality design.
We have a packaging template that needs to be adhered to.
Designer must stick to time frames.
Design needs to be high quality so designers who do not have much experience or can only produce basic designs need not apply.
For this job we will require 1 universal design but we need it for 3 different product types. So the one universal design will then need to be slightly edited to feature a different text, colour and front image. So the packaging is for hair extensions. Pack 1 is for Larkspur Hair Extensions and the second is for Velvet Muse Hair Extensions. This means, we use the same design but just change the product name and text and the image and colour so that the products are easily distinguished by brand name when they are up on display in a store.

The technical info is as follows:
NEW LARKSPUR & VELVET MUSE PACKAGING (DESIGN INFO.)

The following information relates to the NEW Larkspur Hair Extensions & Velvet Muse Hair Extensions Packaging:

1. Packaging DIMENSIONS: see Attachment 1 (Larkspur Packaging Dimensions Template).
Please note: The file to be opened and used in ‘Adobe Illustrator’. The final design likewise will be sent to us in an Adobe Illustrator file.

2. DESIGN: The packaging size will essentially be as per Attachment 2 (Old Larkspur Packaging Blue), but with the following changes:
• The photos, images, background and shape need to be upgraded and redesigned
• The ‘Congratulations’ statement on the rear of the packaging remains the same.
• The HAIR CARE instructions on the rear of the packet will be amended to read as follows:

- Brush hair gently using a loop brush starting at the ends and working towards the scalp while holding the top part to prevent stretching.
- Wash hair in a gentle manner in lukewarm water using a mild moisturising shampoo and conditioner. Do not scrub hair. DO NOT use shampoos and conditioners that contain Alcohol or Sodium Laureth Sulphate as these may attack the bonds on your hair extensions.
- Run fingers through hair daily to make sure the bonds are separated.
- Dry hair by wrapping in a towel or air dry. If using a blow drier use the ‘cool’ setting.
- DO NOT use hot appliances such as blow driers and hair straighteners near the bonds.
- We recommend you visit a salon every four to six weeks to have your extensions checked and readjusted to compensate for your hair growth.

3. The CONTACT information has been changed to read as follows:
LARKSPUR
- For customer support and queries email us at:
enquiry@larkspurhairextensions.com.au

- For information on our range of hair extension products please visit our website:
www.larkspurhairextensions.com.au
VELVET MUSE
wholesale@velvetmuse.com.au

www.velvetmuse.com.au

(note to designer: do not include address and phone information)

Nice to have
• Would like to see more than one choice of design
Would like to see each design in a few different colours
Should not have
• No standard fonts.
No basic designs.
I have attached an example of our current packaging. It must be better quality than this.

```html
<!DOCTYPE html>
<html lang="en">
<head>
<meta charset="utf-8">
<title>Velvet Muse Pre Bonded Hair Extensions – Packaging, Black &amp; Silver</title>
<link rel="stylesheet" href="https://fonts.googleapis.com/css2?family=Cinzel:wght@400;600&family=Playball&family=Open+Sans:wght@600;700&display=swap">
<style>
  :root {
    --board-dark: #3b3e48;
    --board-mid: #6a6c74;
    --board-light: #9a9ba1;
    --silver-1: #f4f4f5;
    --silver-2: #c9cacd;
    --silver-3: #8d8f95;
    --charcoal-1: #2c2e35;
    --charcoal-2: #5a5c63;
    --ink-light: #ffffff;
    --ink-dark: #2a2b30;
    --accent-pink: #d6337f;
    --photo-warm-1: #c9a58a;
    --photo-warm-2: #5b4a44;
    --blonde-1: #e6cfa0;
    --blonde-2: #8c6f58;
  }
  * { margin: 0; padding: 0; box-sizing: border-box; }
  html, body { width: 1200px; height: 900px; overflow: hidden; }
  body { background: var(--board-dark); }
  .board {
    position: relative;
    width: 1200px;
    height: 900px;
    overflow: hidden;
    background: linear-gradient(160deg, var(--board-light) 0%, var(--board-mid) 40%, var(--board-dark) 100%);
    font-family: "Open Sans", Arial, sans-serif;
  }
  .board-swoosh { position: absolute; left: 0; top: 0; width: 1200px; height: 900px; }

  /* showcase photo, left */
  .hero-photo {
    position: absolute; left: 0; top: 140px; width: 390px; height: 360px;
    background: linear-gradient(100deg, var(--photo-warm-2) 0%, var(--photo-warm-1) 45%, var(--blonde-1) 70%, var(--silver-2) 100%);
    border-top-right-radius: 200px 120px;
  }
  .style-band {
    position: absolute; left: 0; top: 508px; width: 390px; height: 46px;
    background: linear-gradient(90deg, rgba(60,62,70,.9), rgba(110,112,120,.6));
    color: var(--ink-light); display: flex; align-items: baseline; gap: 16px; padding: 8px 0 0 38px;
  }
  .style-band .style-name { font-size: 26px; font-weight: 700; }
  .style-band .style-colour { font-size: 20px; font-weight: 600; }
  .view-label {
    position: absolute; left: 40px; top: 824px; color: var(--ink-light);
    font-size: 36px; font-weight: 600;
  }

  /* packaging */
  .pack-front {
    position: absolute; top: 50px; width: 210px; height: 500px; overflow: hidden;
    box-shadow: 0 4px 14px rgba(0,0,0,.35);
  }
  .pack-front--black { left: 390px; background: linear-gradient(180deg, var(--charcoal-2) 0%, var(--silver-2) 30%, var(--charcoal-1) 100%); }
  .pack-front--silver { left: 790px; background: linear-gradient(180deg, var(--silver-1) 0%, var(--silver-2) 55%, var(--silver-3) 100%); }
  .hang-hole {
    position: absolute; top: 46px; width: 12px; height: 12px; border-radius: 50%; background: var(--ink-light);
  }
  .hang-hole--left { left: 66px; } .hang-hole--right { left: 132px; }
  .brand-mark {
    position: absolute; left: 0; width: 100%; text-align: center;
    font-family: "Cinzel", Georgia, serif; font-weight: 400; font-size: 15px; letter-spacing: 1px;
    display: flex; justify-content: center; align-items: center; gap: 6px;
  }
  .brand-mark .brand-dot { width: 12px; height: 12px; border-radius: 50%; background: var(--accent-pink); }
  .brand-mark--on-light { color: var(--ink-dark); }
  .brand-mark--on-dark { color: var(--ink-light); }
  .pack-front .brand-mark { top: 160px; }
  .pack-front--black .brand-mark { top: 160px; }
  .pack-front .brand-mark { top: 164px; }
  .pack-front .brand-mark { top: 160px; }
  .title-panel {
    position: absolute; left: 20px; top: 200px; width: 174px; height: 118px;
    text-align: center; color: var(--ink-light); padding-top: 20px;
  }
  .pack-front--black .title-panel {
    background: linear-gradient(180deg, var(--charcoal-2), var(--charcoal-1));
    border: 1px solid var(--silver-3);
  }
  .pack-front--silver .title-panel {
    background: linear-gradient(180deg, var(--charcoal-2), var(--charcoal-1));
    border: 4px solid var(--silver-1);
  }
  .product-line { font-family: "Cinzel", Georgia, serif; font-size: 21px; line-height: 1.1; }
  .product-type { font-family: "Playball", cursive; font-size: 24px; line-height: 1.2; }
  .pack-photo {
    position: absolute; left: 0; top: 310px; width: 210px; height: 190px;
    background: linear-gradient(120deg, var(--blonde-1) 0%, var(--blonde-2) 55%, var(--photo-warm-1) 100%);
  }
  .pack-flap { position: absolute; top: 450px; width: 244px; height: 362px; }
  .pack-flap--black { left: 518px; }
  .pack-flap--silver { left: 916px; }
  .pack-flap svg { position: absolute; inset: 0; }
  .flap-title { position: absolute; left: 0; top: 130px; width: 100%; padding-left: 14px; text-align: center; color: var(--ink-light); }
  .flap-title .product-line { font-size: 22px; }
  .flap-title .product-type { font-size: 27px; }
  .pack-flap .brand-mark { top: 232px; padding-left: 14px; font-size: 16px; }
</style>
</head>
<body>
<main class="board">
  <svg class="board-swoosh" viewBox="0 0 1200 900" aria-hidden="true">
    <path d="M0 60 C200 120 320 260 400 420 L400 470 C320 300 180 170 0 120 Z" fill="#e9e9ec" opacity=".55"/>
    <path d="M0 20 C220 60 360 200 460 330" stroke="#f2f2f4" stroke-width="6" fill="none" opacity=".6"/>
    <path d="M140 0 C260 140 320 300 330 500" stroke="#dcdce0" stroke-width="30" fill="none" opacity=".25"/>
  </svg>

  <div class="hero-photo" role="img" aria-label="Photograph of two models, one brunette and one blonde, wearing long hair extensions"></div>
  <div class="style-band"><span class="style-name">2nd Style</span><span class="style-colour">Black &amp; silver</span></div>

  <!-- pack in black and silver -->
  <section class="pack-front pack-front--black">
    <span class="hang-hole hang-hole--left"></span><span class="hang-hole hang-hole--right"></span>
    <div class="brand-mark brand-mark--on-dark" style="top:140px"><span class="brand-dot"></span>Velvet Muse</div>
    <div class="title-panel">
      <p class="product-line">Pre Bonded</p>
      <p class="product-type">Hair Extensions</p>
    </div>
    <div class="pack-photo" role="img" aria-label="Photograph of a blonde model with long wavy hair"></div>
  </section>
  <section class="pack-flap pack-flap--black">
    <svg viewBox="0 0 244 362" aria-hidden="true">
      <defs>
        <linearGradient id="flapBlack" x1="0" y1="0" x2="1" y2="1">
          <stop offset="0" stop-color="#8a8c92"/><stop offset=".5" stop-color="#4a4c53"/><stop offset="1" stop-color="#26282e"/>
        </linearGradient>
      </defs>
      <path d="M2 150 Q6 40 96 22 L242 0 L242 360 L2 360 Z" fill="url(#flapBlack)" stroke="#c9cacd" stroke-width="2"/>
      <path d="M2 300 C80 260 160 300 242 250 L242 290 C160 330 80 300 2 340 Z" fill="#e6e6e9" opacity=".45"/>
    </svg>
    <div class="flap-title">
      <p class="product-line">Pre Bonded</p>
      <p class="product-type">Hair Extensions</p>
    </div>
    <div class="brand-mark brand-mark--on-dark"><span class="brand-dot"></span>Velvet Muse</div>
  </section>

  <!-- pack in silver -->
  <section class="pack-front pack-front--silver">
    <span class="hang-hole hang-hole--left"></span><span class="hang-hole hang-hole--right"></span>
    <div class="title-panel" style="top:96px;height:150px;padding-top:10px">
      <div class="brand-mark brand-mark--on-dark" style="position:static;margin-bottom:14px"><span class="brand-dot"></span>Velvet Muse</div>
      <p class="product-line">Pre Bonded</p>
      <p class="product-type">Hair Extensions</p>
    </div>
    <div class="pack-photo" role="img" aria-label="Photograph of a blonde model with long wavy hair"></div>
  </section>
  <section class="pack-flap pack-flap--silver">
    <svg viewBox="0 0 244 362" aria-hidden="true">
      <defs>
        <linearGradient id="flapSilver" x1="0" y1="0" x2="1" y2="1">
          <stop offset="0" stop-color="#9a9ca2"/><stop offset=".5" stop-color="#55575e"/><stop offset="1" stop-color="#2e3036"/>
        </linearGradient>
      </defs>
      <path d="M2 150 Q6 40 96 22 L242 0 L242 360 L2 360 Z" fill="url(#flapSilver)" stroke="#e6e6e9" stroke-width="2"/>
      <path d="M2 290 C80 250 160 290 242 240 L242 280 C160 320 80 290 2 330 Z" fill="#f0f0f2" opacity=".5"/>
    </svg>
    <div class="flap-title">
      <p class="product-line">Pre Bonded</p>
      <p class="product-type">Hair Extensions</p>
    </div>
  </section>

  <p class="view-label">Front look</p>
</main>
</body>
</html>
```